Business Card Design Project

Want a modern business card.
Concern is that our email address is long and thus poses a design challenge.
Items like the company name can be omitted from text as it will be available via the logo.

Example:
Gerald Tunstall
President / CEO
Cell 555.304.1182
Office 555.617.2093
geraldt@korvantsolutionsgroup.example
www.korvantsolutionsgroup.example

Target Market(s)

Technical and executive level members of Information Technology companies in the Healthcare industry.

Industry/Entity Type

Business

Colors

Designer to choose colors to be used in the design.

Requirements
Nice to have
• Raised logo, but I am open.

```html
<!DOCTYPE html>
<html lang="en">
<head>
<meta charset="utf-8">
<title>Korvant Solutions Group – Business Card</title>
<link rel="stylesheet" href="https://fonts.googleapis.com/css2?family=Open+Sans:wght@400;600;700&display=swap">
<style>
  :root {
    --page-bg: #f1f2f4;
    --back-blue-light: #2a68cc;
    --back-blue: #1a52b5;
    --back-blue-deep: #1546a3;
    --front-sky-light: #eef7fc;
    --front-sky: #c6e2f3;
    --band-light: #5b9ad6;
    --band: #2f6fc0;
    --band-deep: #2560b0;
    --silver: #d9dee4;
    --silver-dark: #9aa5b1;
    --navy: #1f3a7c;
    --accent-red: #d4161d;
    --white: #ffffff;
    --card-shadow: 0 18px 30px rgba(20, 40, 80, 0.18);
  }

  * { box-sizing: border-box; margin: 0; padding: 0; }

  html, body {
    width: 1200px;
    height: 900px;
    overflow: hidden;
  }

  body {
    background: var(--page-bg);
    font-family: "Open Sans", Arial, sans-serif;
    position: relative;
  }

  .card {
    position: absolute;
    top: 300px;
    width: 520px;
    height: 300px;
    border-radius: 24px;
    overflow: hidden;
    box-shadow: var(--card-shadow);
  }

  /* ---------- Back side ---------- */
  .card--back {
    left: 50px;
    background: linear-gradient(160deg, var(--back-blue-light) 0%, var(--back-blue) 50%, var(--back-blue-deep) 100%);
  }

  .card--back .texture {
    position: absolute;
    inset: 0;
    background: radial-gradient(ellipse at 80% 20%, rgba(255,255,255,0.14), rgba(255,255,255,0) 60%);
  }

  .card--back .brand-name {
    position: absolute;
    left: 0;
    right: 0;
    top: 126px;
    text-align: center;
    color: var(--white);
    font-weight: 700;
    font-size: 34px;
    letter-spacing: 0.5px;
  }

  /* ---------- Front side ---------- */
  .card--front {
    left: 630px;
    background: linear-gradient(135deg, var(--front-sky-light) 0%, var(--front-sky) 100%);
  }

  .card--front .texture {
    position: absolute;
    inset: 0;
    background: radial-gradient(ellipse at 90% 10%, rgba(120,180,225,0.35), rgba(255,255,255,0) 65%);
  }

  .card--front .brand-name {
    position: absolute;
    left: 36px;
    top: 40px;
    color: var(--navy);
    font-weight: 700;
    font-size: 28px;
    letter-spacing: 0.3px;
  }

  .person {
    position: absolute;
    left: 36px;
    top: 128px;
  }

  .person__name {
    color: var(--accent-red);
    font-weight: 700;
    font-size: 21px;
    line-height: 1.15;
  }

  .person__title {
    color: var(--navy);
    font-weight: 600;
    font-size: 13px;
    margin-top: 3px;
  }

  .contact-band {
    position: absolute;
    left: 0;
    right: 0;
    top: 188px;
    height: 90px;
    background: linear-gradient(180deg, var(--band-light) 0%, var(--band) 45%, var(--band-deep) 100%);
    border-top: 3px solid var(--silver);
    border-bottom: 3px solid var(--silver);
    box-shadow: 0 -1px 0 var(--silver-dark), 0 1px 0 var(--silver-dark);
  }

  .contact-list {
    list-style: none;
    position: absolute;
    left: 36px;
    top: 196px;
  }

  .contact-list li {
    display: flex;
    align-items: center;
    gap: 7px;
    height: 19px;
    color: var(--white);
    font-size: 14.5px;
    letter-spacing: 0.2px;
  }

  .contact-list svg {
    width: 13px;
    height: 13px;
    flex: none;
  }
</style>
</head>
<body>

  <section class="card card--back" aria-label="Card back">
    <div class="texture" role="img" aria-label="Fine blue line grid background"></div>
    <div class="brand-name">Korvant Solutions Group</div>
  </section>

  <section class="card card--front" aria-label="Card front">
    <div class="texture" role="img" aria-label="Fine pale blue line grid background"></div>
    <div class="brand-name">Korvant Solutions Group</div>

    <div class="person">
      <div class="person__name">Gerald Tunstall</div>
      <div class="person__title">President / CEO</div>
    </div>

    <div class="contact-band"></div>

    <ul class="contact-list">
      <li>
        <svg viewBox="0 0 14 14" aria-hidden="true"><rect x="3" y="1" width="8" height="12" rx="1.5" fill="var(--accent-red)"/><rect x="4.5" y="2.8" width="5" height="6" fill="var(--white)"/><circle cx="7" cy="11" r="0.9" fill="var(--white)"/></svg>
        <span>555.304.1182</span>
      </li>
      <li>
        <svg viewBox="0 0 14 14" aria-hidden="true"><path d="M3 1.5 L5.2 1 L6.3 4.2 L4.8 5.3 C5.6 7 6.9 8.3 8.6 9.2 L9.8 7.7 L13 8.8 L12.5 11 C12.3 12 11.4 12.6 10.4 12.4 C5.8 11.5 2.4 8.1 1.5 3.5 C1.4 2.5 2 1.7 3 1.5 Z" fill="var(--accent-red)"/></svg>
        <span>555.617.2093</span>
      </li>
      <li>
        <svg viewBox="0 0 14 14" aria-hidden="true"><rect x="1" y="3" width="12" height="9" rx="1" fill="var(--accent-red)"/><path d="M1.5 3.5 L7 8 L12.5 3.5" fill="none" stroke="var(--white)" stroke-width="1.1"/></svg>
        <span>geraldt@korvantsolutionsgroup.example</span>
      </li>
      <li>
        <svg viewBox="0 0 14 14" aria-hidden="true"><circle cx="7" cy="7" r="6" fill="var(--accent-red)"/><g fill="none" stroke="var(--white)" stroke-width="0.9"><ellipse cx="7" cy="7" rx="2.6" ry="6"/><line x1="1" y1="7" x2="13" y2="7"/><line x1="2" y1="4" x2="12" y2="4"/><line x1="2" y1="10" x2="12" y2="10"/></g></svg>
        <span>www.korvantsolutionsgroup.example</span>
      </li>
    </ul>
  </section>

</body>
</html>
```